SEO wiki for a know-how website (rankvale.ch)

Hi,

i need a know-how wiki for an SEO website that looks similar to:

http://demo.plinkora.com/#knowhow

With following know-how categories instead of "account settings" and "API questions":
- Content SEO
- Technical SEO
- Link building
- Influencer marketing
- paid marketing
- analytics & measurement

So i Need the following pages:
1. Landing page with the categories, the search bar and the side-bar
- Sidebar has latest articles, popular articles and categories (in this order)
- On top a nice logo
- on top right -> blog, contact
- on top right below -> social media buttons: brivella, chirpnet

2. a blog site with
- headline
- sub-headline
- date, name
- rating with 5 "know-how" stars
- picture
- article
- info about the author
- related articles
- integration of comment plugin TALVEO

Target Market(s)

SEO folks

Industry/Entity Type

Seo

Logo Text

Do-it yourself SEO

Number of Pages Required

2 page

Font styles to use
Sans Serif

Colors

Designer to choose colors to be used in the design.

```html
<!DOCTYPE html>
<html lang="en">
<head>
<meta charset="utf-8">
<title>Rankvale – Know-how</title>
<link rel="stylesheet" href="https://fonts.googleapis.com/css2?family=Nunito:wght@300;400;600;800&display=swap">
<style>
  :root{
    --brand:#35a9e1;
    --brand-dark:#1b7fb4;
    --ink:#3a3f44;
    --ink-soft:#555b61;
    --muted:#6b7177;
    --rule:#dcdfe2;
    --footer:#eeeeee;
    --white:#ffffff;
  }
  *{box-sizing:border-box;margin:0;padding:0}
  html,body{width:988px;height:1200px;overflow:hidden;background:var(--white)}
  body{font-family:"Nunito",Arial,sans-serif;color:var(--ink);position:relative}
  a{color:inherit;text-decoration:none}
  ul{list-style:none}

  .site-header{position:absolute;left:0;top:0;width:988px;height:90px}
  .brand{position:absolute;left:74px;top:30px;font-size:32px;font-weight:800;color:var(--brand);letter-spacing:.2px}
  .main-nav{position:absolute;left:701px;top:43px;display:flex;gap:34px;font-size:13px;color:var(--ink-soft);letter-spacing:.3px}
  .social{position:absolute;left:846px;top:42px;display:flex;gap:10px;font-size:11px;font-weight:600;color:var(--brand-dark)}
  .social a{display:flex;align-items:center;gap:4px}
  .social a::before{content:"";width:8px;height:8px;background:var(--brand);border-radius:2px}

  .hero{position:absolute;left:0;top:90px;width:988px;height:280px}
  .hero-bg{position:absolute;inset:0;background:linear-gradient(135deg,#3aabe2 0%,#2f9fd9 45%,#3cafe4 100%)}
  .hero-title{position:absolute;left:0;right:0;top:58px;text-align:center;color:var(--white);font-size:32px;font-weight:400;letter-spacing:.5px}
  .search{position:absolute;left:162px;top:132px;width:664px;height:56px;display:flex;border-radius:2px;overflow:hidden}
  .search-field{flex:1;background:var(--white);display:flex;align-items:center;padding-left:22px;font-size:14px;color:var(--ink-soft)}
  .search-btn{width:104px;background:var(--brand-dark);color:var(--white);display:flex;align-items:center;justify-content:center;font-size:16px;letter-spacing:.3px}

  .categories{position:absolute;left:82px;top:418px;width:572px}
  .section-title{font-size:22px;font-weight:400;color:var(--ink);height:41px}
  .cat-row{display:grid;grid-template-columns:313px 259px;border-top:1px solid var(--rule);height:217px;padding-top:14px}
  .cat-head{display:flex;align-items:center;gap:10px;font-size:16px;color:var(--ink);height:24px;padding-left:4px}
  .cat-head svg{width:18px;height:18px;flex:none}
  .cat-list{margin:8px 0 0 34px}
  .cat-list li,.side-list li{display:flex;align-items:center;gap:6px}
  .cat-list li{height:24.5px;font-size:13px;color:var(--ink-soft)}
  .doc{width:11px;height:13px;flex:none}

  .sidebar{position:absolute;left:677px;top:428px;height:674px;border-left:1px solid var(--rule);padding-left:23px;width:260px}
  .side-title{font-size:15px;color:var(--ink);margin-top:-2px;height:26px}
  .side-list{margin-top:0}
  .side-list li{height:24.5px;font-size:11px;color:var(--muted)}
  .side-block{position:absolute;left:23px}
  .count{width:13px;height:13px;border-radius:50%;background:var(--brand);color:var(--white);font-size:7.5px;font-weight:800;display:flex;align-items:center;justify-content:center;flex:none}

  .site-footer{position:absolute;left:0;top:1136px;width:988px;height:64px;background:var(--footer);display:flex;align-items:center;justify-content:center;font-size:10.5px;color:var(--ink-soft)}
</style>
</head>
<body>
<svg width="0" height="0" style="position:absolute">
  <symbol id="i-doc" viewBox="0 0 11 13"><path d="M1 .5h6l3.5 3.5v8.5H1z M7 .5V4h3.5" fill="none" stroke="#555b61" stroke-width=".9"/><path d="M3 6.5h5M3 8.5h5M3 10.5h5" stroke="#555b61" stroke-width=".8"/></symbol>
</svg>

<header class="site-header">
  <a class="brand" href="#">Rankvale</a>
  <nav class="main-nav"><a href="#">BLOG</a><a href="#">CONTACT</a></nav>
  <div class="social"><a href="#">brivella</a><a href="#">chirpnet</a></div>
</header>

<section class="hero">
  <div class="hero-bg" role="img" aria-label="Blue low-poly geometric background"></div>
  <h1 class="hero-title">RANKVALE</h1>
  <div class="search">
    <div class="search-field">Have a question? Ask or enter a search term</div>
    <div class="search-btn">SEARCH</div>
  </div>
</section>

<main class="categories">
  <h2 class="section-title">Article Categories</h2>

  <div class="cat-row">
    <div>
      <div class="cat-head"><svg viewBox="0 0 18 18"><circle cx="7.5" cy="7.5" r="5.5" fill="none" stroke="#3a3f44" stroke-width="2.2"/><path d="M11.5 11.5l5 5" stroke="#3a3f44" stroke-width="2.6" stroke-linecap="round"/></svg>Content SEO (6)</div>
      <ul class="cat-list">
        <li><svg class="doc"><use href="#i-doc"/></svg>Porro quisquam est qui dolorem</li>
        <li><svg class="doc"><use href="#i-doc"/></svg>Dolorem ipsum quia dolor</li>
        <li><svg class="doc"><use href="#i-doc"/></svg>Quisquam est qui dolorem ipsum</li>
        <li><svg class="doc"><use href="#i-doc"/></svg>Neque porro quisquam est qui</li>
        <li><svg class="doc"><use href="#i-doc"/></svg>Dolorem ipsum quia dolor</li>
        <li><svg class="doc"><use href="#i-doc"/></svg>Quisquam est qui dolorem</li>
      </ul>
    </div>
    <div>
      <div class="cat-head" style="padding-left:0"><svg viewBox="0 0 18 18"><rect x="1" y="2" width="16" height="11" rx="1" fill="none" stroke="#3a3f44" stroke-width="1.8"/><rect x="1" y="10" width="16" height="3" fill="#3a3f44"/><path d="M6 16h6M9 13v3" stroke="#3a3f44" stroke-width="1.8"/></svg>Technical SEO (9)</div>
      <ul class="cat-list" style="margin-left:30px">
        <li><svg class="doc"><use href="#i-doc"/></svg>Porro quisquam est qui dolorem</li>
        <li><svg class="doc"><use href="#i-doc"/></svg>Dolorem ipsum quia dolor</li>
        <li><svg class="doc"><use href="#i-doc"/></svg>Quisquam est qui dolorem ipsum</li>
        <li><svg class="doc"><use href="#i-doc"/></svg>Neque porro quisquam est qui</li>
        <li><svg class="doc"><use href="#i-doc"/></svg>Dolorem ipsum quia dolor</li>
        <li><svg class="doc"><use href="#i-doc"/></svg>Quisquam est qui dolorem</li>
      </ul>
    </div>
  </div>

  <div class="cat-row">
    <div>
      <div class="cat-head"><svg viewBox="0 0 18 18"><rect x="1" y="2" width="8" height="5" rx="2.5" transform="rotate(40 5 4.5)" fill="none" stroke="#3a3f44" stroke-width="1.8"/><rect x="8" y="10" width="8" height="5" rx="2.5" transform="rotate(40 12 12.5)" fill="none" stroke="#3a3f44" stroke-width="1.8"/><path d="M6.5 7.5l4 3.5" stroke="#3a3f44" stroke-width="1.8"/></svg>Link building (8)</div>
      <ul class="cat-list">
        <li><svg class="doc"><use href="#i-doc"/></svg>Porro quisquam est qui dolorem</li>
        <li><svg class="doc"><use href="#i-doc"/></svg>Dolorem ipsum quia dolor</li>
        <li><svg class="doc"><use href="#i-doc"/></svg>Quisquam est qui dolorem ipsum</li>
        <li><svg class="doc"><use href="#i-doc"/></svg>Neque porro quisquam est qui</li>
        <li><svg class="doc"><use href="#i-doc"/></svg>Dolorem ipsum quia dolor</li>
        <li><svg class="doc"><use href="#i-doc"/></svg>Quisquam est qui dolorem</li>
      </ul>
    </div>
    <div>
      <div class="cat-head" style="padding-left:2px"><svg viewBox="0 0 18 18"><circle cx="9" cy="9" r="7.2" fill="none" stroke="#3a3f44" stroke-width="2.2"/><circle cx="9" cy="9" r="3.2" fill="none" stroke="#3a3f44" stroke-width="1.8"/><path d="M3.8 3.8l3 3M14.2 3.8l-3 3M3.8 14.2l3-3M14.2 14.2l-3-3" stroke="#3a3f44" stroke-width="2.4"/></svg>Influencer marketing (7)</div>
      <ul class="cat-list" style="margin-left:30px">
        <li><svg class="doc"><use href="#i-doc"/></svg>Porro quisquam est qui dolorem</li>
        <li><svg class="doc"><use href="#i-doc"/></svg>Dolorem ipsum quia dolor</li>
        <li><svg class="doc"><use href="#i-doc"/></svg>Quisquam est qui dolorem ipsum</li>
        <li><svg class="doc"><use href="#i-doc"/></svg>Neque porro quisquam est qui</li>
        <li><svg class="doc"><use href="#i-doc"/></svg>Dolorem ipsum quia dolor</li>
        <li><svg class="doc"><use href="#i-doc"/></svg>Quisquam est qui dolorem</li>
      </ul>
    </div>
  </div>

  <div class="cat-row">
    <div>
      <div class="cat-head"><svg viewBox="0 0 18 18"><path d="M1 1h7l2 2v4H1z" fill="#3a3f44"/><path d="M1 1v14h5" fill="none" stroke="#3a3f44" stroke-width="1.8"/><path d="M7 5h6l4 4v8H7z" fill="none" stroke="#3a3f44" stroke-width="1.8"/><path d="M13 5v4h4" fill="#3a3f44"/></svg>Paid marketing (6)</div>
      <ul class="cat-list">
        <li><svg class="doc"><use href="#i-doc"/></svg>Porro quisquam est qui dolorem</li>
        <li><svg class="doc"><use href="#i-doc"/></svg>Dolorem ipsum quia dolor</li>
        <li><svg class="doc"><use href="#i-doc"/></svg>Quisquam est qui dolorem ipsum</li>
        <li><svg class="doc"><use href="#i-doc"/></svg>Neque porro quisquam est qui</li>
        <li><svg class="doc"><use href="#i-doc"/></svg>Dolorem ipsum quia dolor</li>
        <li><svg class="doc"><use href="#i-doc"/></svg>Quisquam est qui dolorem</li>
      </ul>
    </div>
    <div>
      <div class="cat-head" style="padding-left:0"><svg viewBox="0 0 18 18"><path d="M1 2v14h16" fill="none" stroke="#3a3f44" stroke-width="1.6"/><path d="M5 14V9M8 14V6M11 14V8M14 14V4" stroke="#3a3f44" stroke-width="2"/></svg>Analytics &amp; measurement (5)</div>
      <ul class="cat-list" style="margin-left:30px">
        <li><svg class="doc"><use href="#i-doc"/></svg>Porro quisquam est qui dolorem</li>
        <li><svg class="doc"><use href="#i-doc"/></svg>Dolorem ipsum quia dolor</li>
        <li><svg class="doc"><use href="#i-doc"/></svg>Quisquam est qui dolorem ipsum</li>
        <li><svg class="doc"><use href="#i-doc"/></svg>Neque porro quisquam est qui</li>
        <li><svg class="doc"><use href="#i-doc"/></svg>Dolorem ipsum quia dolor</li>
        <li><svg class="doc"><use href="#i-doc"/></svg>Quisquam est qui dolorem</li>
      </ul>
    </div>
  </div>
</main>

<aside class="sidebar">
  <div class="side-block" style="top:0">
    <h3 class="side-title">Latest Articles</h3>
    <ul class="side-list" style="margin-top:3px">
      <li><svg class="doc"><use href="#i-doc"/></svg>How Secure Is My Password?</li>
      <li><svg class="doc"><use href="#i-doc"/></svg>What Technologies Are Used?</li>
      <li><svg class="doc"><use href="#i-doc"/></svg>How Do I Change My Password?</li>
      <li><svg class="doc"><use href="#i-doc"/></svg>Can I Change My Username?</li>
      <li><svg class="doc"><use href="#i-doc"/></svg>Dolorem ipsum quia dolor ?</li>
      <li><svg class="doc"><use href="#i-doc"/></svg>Quisquam est qui dolorem ?</li>
    </ul>
  </div>
  <div class="side-block" style="top:227px">
    <h3 class="side-title">Popular Articles</h3>
    <ul class="side-list" style="margin-top:3px">
      <li><svg class="doc"><use href="#i-doc"/></svg>Quisquam est qui dolorem ?</li>
      <li><svg class="doc"><use href="#i-doc"/></svg>What Technologies Are Used?</li>
      <li><svg class="doc"><use href="#i-doc"/></svg>How Secure Is My Password?</li>
      <li><svg class="doc"><use href="#i-doc"/></svg>How Do I Change My Password?</li>
      <li><svg class="doc"><use href="#i-doc"/></svg>Can I Change My Username?</li>
      <li><svg class="doc"><use href="#i-doc"/></svg>Quisquam est qui dolorem ?</li>
    </ul>
  </div>
  <div class="side-block" style="top:448px">
    <h3 class="side-title">Categories</h3>
    <ul class="side-list" style="margin-top:3px">
      <li><span class="count">6</span>Content SEO</li>
      <li><span class="count">9</span>Technical SEO</li>
      <li><span class="count">8</span>Link building</li>
      <li><span class="count">7</span>Influencer marketing</li>
      <li><span class="count">6</span>Paid marketing</li>
      <li><span class="count">5</span>Analytics &amp; measurement</li>
    </ul>
  </div>
</aside>

<footer class="site-footer">Copyright © 2017. All Rights Reserved</footer>
</body>
</html>
```